The Orchard of Virtue Customized for my Business

Hi! I am interested in getting some design ideas to take this Orchard of Virtue and put a bit of branding of my business into it. Open to any and all designs, this is intended to put on a 20"x24" or 16"x20" canvas so I can have it in my office for team training purposes. I have included a picture of the wall this canvas will go on. Thank you!

```html
<!DOCTYPE html>
<html lang="en">
<head>
<meta charset="utf-8">
<title>The Orchard of Virtue</title>
<link href="https://fonts.googleapis.com/css2?family=Roboto:wght@400;500;700;900&display=swap" rel="stylesheet">
<style>
  :root {
    --blue: #2b9cd8;
    --blue-mid: #3aa6e0;
    --blue-light: #bfe1f5;
    --blue-pale: #e8f4fc;
    --charcoal: #3b3e44;
    --ink: #1f2226;
    --white: #ffffff;
  }
  html, body {
    margin: 0;
    padding: 0;
    width: 1200px;
    height: 1200px;
    overflow: hidden;
    background: var(--white);
  }
  .poster {
    display: block;
    width: 1200px;
    height: 1200px;
    font-family: "Roboto", Arial, sans-serif;
  }
  .side-band { fill: var(--blue); }
  .band-rule { stroke: var(--white); stroke-width: 4; }
  .icon-rule { stroke: var(--blue); stroke-width: 2; }
  .pyramid-frame { fill: var(--charcoal); }
  .cell-pale { fill: var(--blue-pale); }
  .cell-light { fill: var(--blue-light); }
  .cell-mid { fill: var(--blue-mid); }
  .cell-white { fill: var(--white); }
  .block-title {
    font-weight: 900;
    font-size: 7.2px;
    fill: var(--ink);
    text-anchor: middle;
  }
  .block-title.accent { fill: var(--blue); }
  .block-text {
    font-weight: 500;
    font-size: 4.9px;
    fill: var(--ink);
    text-anchor: middle;
  }
  .virtue-name {
    font-weight: 900;
    font-size: 9.5px;
    fill: var(--white);
    text-anchor: middle;
    letter-spacing: 0.3px;
  }
  .virtue-note {
    font-weight: 500;
    font-size: 6px;
    fill: var(--ink);
    text-anchor: middle;
  }
  .icon {
    fill: none;
    stroke: var(--blue);
    stroke-width: 2.2;
    stroke-linecap: round;
    stroke-linejoin: round;
  }
  .badge { fill: var(--charcoal); stroke: var(--white); stroke-width: 4; }
  .badge-name {
    font-weight: 700;
    font-size: 15px;
    fill: var(--blue);
    text-anchor: middle;
    letter-spacing: 0.5px;
  }
  .headline {
    font-weight: 700;
    font-size: 37px;
    text-anchor: middle;
    letter-spacing: 0.5px;
  }
  .headline-lead { fill: var(--blue); }
  .headline-key { fill: var(--white); }
  .credit {
    font-weight: 700;
    font-size: 5.5px;
    fill: var(--ink);
    text-anchor: middle;
  }
</style>
</head>
<body>
<svg class="poster" viewBox="0 0 980 980" width="1200" height="1200" xmlns="http://www.w3.org/2000/svg" aria-labelledby="poster-title">
  <title id="poster-title">The Orchard of Virtue</title>
  <defs>
    <clipPath id="row-1"><polygon points="459,290 521,290 554,348 426,348"/></clipPath>
    <clipPath id="row-2"><polygon points="421,356 559,356 604,436 376,436"/></clipPath>
    <clipPath id="row-3"><polygon points="371.5,444 608.5,444 660.6,536 319.4,536"/></clipPath>
    <clipPath id="row-4"><polygon points="316,542 664,542 715,632 265,632"/></clipPath>
    <clipPath id="row-5"><polygon points="260.5,640 719.5,640 770.4,730 209.6,730"/></clipPath>
  </defs>

  <g class="icon-shelves">
    <line class="icon-rule" x1="330" y1="343" x2="380" y2="343"/>
    <line class="icon-rule" x1="272" y1="440" x2="320" y2="440"/>
    <line class="icon-rule" x1="218" y1="539" x2="262" y2="539"/>
    <line class="icon-rule" x1="162" y1="636" x2="206" y2="636"/>
    <line class="icon-rule" x1="105" y1="733" x2="150" y2="733"/>
    <line class="icon-rule" x1="600" y1="343" x2="650" y2="343"/>
    <line class="icon-rule" x1="660" y1="440" x2="708" y2="440"/>
    <line class="icon-rule" x1="718" y1="539" x2="762" y2="539"/>
    <line class="icon-rule" x1="774" y1="636" x2="818" y2="636"/>
    <line class="icon-rule" x1="830" y1="733" x2="875" y2="733"/>
  </g>

  <polygon class="side-band" points="490,139 885,825 95,825"/>
  <g class="band-rules">
    <line class="band-rule" x1="372.5" y1="343" x2="607.5" y2="343"/>
    <line class="band-rule" x1="316.6" y1="440" x2="663.4" y2="440"/>
    <line class="band-rule" x1="259.6" y1="539" x2="720.4" y2="539"/>
    <line class="band-rule" x1="203.7" y1="636" x2="776.3" y2="636"/>
    <line class="band-rule" x1="148" y1="733" x2="832" y2="733"/>
  </g>

  <polygon class="pyramid-frame" points="490,224 830,825 150,825"/>

  <g class="tier" clip-path="url(#row-1)">
    <rect class="cell-pale" x="400" y="290" width="180" height="58"/>
  </g>
  <g class="tier" clip-path="url(#row-2)">
    <rect class="cell-white" x="370" y="356" width="120" height="80"/>
    <rect class="cell-light" x="490" y="356" width="120" height="80"/>
  </g>
  <g class="tier" clip-path="url(#row-3)">
    <rect class="cell-light" x="315" y="444" width="118.3" height="92"/>
    <rect class="cell-mid" x="433.3" y="444" width="113.4" height="92"/>
    <rect class="cell-white" x="546.7" y="444" width="118" height="92"/>
  </g>
  <g class="tier" clip-path="url(#row-4)">
    <rect class="cell-light" x="260" y="542" width="117.5" height="90"/>
    <rect class="cell-white" x="377.5" y="542" width="112.5" height="90"/>
    <rect class="cell-light" x="490" y="542" width="112.5" height="90"/>
    <rect class="cell-mid" x="602.5" y="542" width="117.5" height="90"/>
  </g>
  <g class="tier" clip-path="url(#row-5)">
    <rect class="cell-pale" x="205" y="640" width="116.8" height="90"/>
    <rect class="cell-light" x="321.8" y="640" width="112.2" height="90"/>
    <rect class="cell-mid" x="434" y="640" width="112.2" height="90"/>
    <rect class="cell-white" x="546.2" y="640" width="112.2" height="90"/>
    <rect class="cell-light" x="658.4" y="640" width="116.6" height="90"/>
  </g>

  <g class="block">
    <text class="block-title" x="490" y="306">COMPETITIVE</text>
    <text class="block-title" x="490" y="314.5">GREATNESS</text>
    <text class="block-text" x="490" y="324">Be at our best when your</text>
    <text class="block-text" x="490" y="330.5">best is needed. Enjoyment of</text>
    <text class="block-text" x="490" y="337">a difficult challenge</text>
  </g>

  <g class="block">
    <text class="block-title" x="448" y="393">POISE</text>
    <text class="block-text" x="448" y="402">Just being yourself.</text>
    <text class="block-text" x="448" y="408.5">Being at ease in any situation.</text>
    <text class="block-text" x="448" y="415">Never fighting yourself.</text>
  </g>
  <g class="block">
    <text class="block-title" x="534" y="393">CONFIDENCE</text>
    <text class="block-text" x="534" y="402">Respect without fear.</text>
    <text class="block-text" x="534" y="408.5">May come from being</text>
    <text class="block-text" x="534" y="415">prepared and keeping all things</text>
    <text class="block-text" x="534" y="421.5">in proper perspective.</text>
  </g>

  <g class="block">
    <text class="block-title" x="392" y="477">CONDITION</text>
    <text class="block-text" x="392" y="486">Mental-Moral-Physical.</text>
    <text class="block-text" x="392" y="492.5">Rest, exercise &amp; diet</text>
    <text class="block-text" x="392" y="499">must be considered.</text>
    <text class="block-text" x="392" y="505.5">Moderation must be practiced.</text>
    <text class="block-text" x="392" y="512">Dissipation must be eliminated.</text>
  </g>
  <g class="block">
    <text class="block-title" x="490" y="477">SKILL</text>
    <text class="block-text" x="490" y="486">Knowledge of and the ability</text>
    <text class="block-text" x="490" y="492.5">to properly and quickly</text>
    <text class="block-text" x="490" y="499">execute the fundamentals.</text>
  </g>
  <g class="block">
    <text class="block-title accent" x="594" y="477">TEAM SPIRIT</text>
    <text class="block-text" x="594" y="486">A genuine consideration</text>
    <text class="block-text" x="594" y="492.5">for others. An eagerness to</text>
    <text class="block-text" x="594" y="499">sacrifice personal interests</text>
    <text class="block-text" x="594" y="505.5">of glory for the welfare of all.</text>
  </g>

  <g class="block">
    <text class="block-title" x="336" y="574">SELF-CONTROL</text>
    <text class="block-text" x="336" y="583">Practice self discipline and</text>
    <text class="block-text" x="336" y="589.5">keep emotions under control.</text>
    <text class="block-text" x="336" y="596">Good judgement and common</text>
    <text class="block-text" x="336" y="602.5">sense are essential.</text>
  </g>
  <g class="block">
    <text class="block-title accent" x="434" y="574">ALERTNESS</text>
    <text class="block-text" x="434" y="583">Be observing constantly.</text>
    <text class="block-text" x="434" y="589.5">Stay open minded.</text>
    <text class="block-text" x="434" y="596">Be eager to learn and improve.</text>
  </g>
  <g class="block">
    <text class="block-title" x="546" y="574">INITIATIVE</text>
    <text class="block-text" x="546" y="583">Cultivate the ability to make</text>
    <text class="block-text" x="546" y="589.5">decisions and think alone.</text>
    <text class="block-text" x="546" y="596">Do not be afraid of failure</text>
    <text class="block-text" x="546" y="602.5">but learn from it.</text>
  </g>
  <g class="block">
    <text class="block-title" x="647" y="574">INTENTNESS</text>
    <text class="block-text" x="647" y="583">Set a realistic goal.</text>
    <text class="block-text" x="647" y="589.5">Concentrate on its achievement</text>
    <text class="block-text" x="647" y="596">by resisting all temptations</text>
    <text class="block-text" x="647" y="602.5">and being determined</text>
    <text class="block-text" x="647" y="609">and persistant.</text>
  </g>

  <g class="block">
    <text class="block-title accent" x="287" y="679">INDUSTRIOUSNESS</text>
    <text class="block-text" x="287" y="688">There is no substitute</text>
    <text class="block-text" x="287" y="694.5">for work. Worthwhile results</text>
    <text class="block-text" x="287" y="701">come from hardwork</text>
    <text class="block-text" x="287" y="707.5">and careful planning</text>
  </g>
  <g class="block">
    <text class="block-title" x="378" y="679">FRIENDSHIP</text>
    <text class="block-text" x="378" y="688">Comes from mutual esteem,</text>
    <text class="block-text" x="378" y="694.5">respect and devotion.</text>
    <text class="block-text" x="378" y="701">Like marriage it must not be taken</text>
    <text class="block-text" x="378" y="707.5">for granted but requires</text>
    <text class="block-text" x="378" y="714">a joint effort</text>
  </g>
  <g class="block">
    <text class="block-title" x="490" y="679">LOYALTY</text>
    <text class="block-text" x="490" y="688">To yourself and to all those</text>
    <text class="block-text" x="490" y="694.5">depending upon you.</text>
    <text class="block-text" x="490" y="701">Keep your self-respect.</text>
  </g>
  <g class="block">
    <text class="block-title accent" x="602" y="679">COOPERATION</text>
    <text class="block-text" x="602" y="688">With all levels of your co-workers.</text>
    <text class="block-text" x="602" y="694.5">Listen if you want to be heard.</text>
    <text class="block-text" x="602" y="701">Be interested in finding</text>
    <text class="block-text" x="602" y="707.5">the best way,</text>
    <text class="block-text" x="602" y="714">not in having your own way.</text>
  </g>
  <g class="block">
    <text class="block-title" x="704" y="679">ENTHUSIASMS</text>
    <text class="block-text" x="705" y="690">With all levels of your co-workers.</text>
    <text class="block-text" x="705" y="696.5">Listen if you want to be heard.</text>
    <text class="block-text" x="705" y="703">Be interested in finding</text>
    <text class="block-text" x="705" y="709.5">the best way,</text>
    <text class="block-text" x="705" y="716">not in having your own way.</text>
  </g>

  <g class="virtue" transform="translate(428,292) rotate(-60)">
    <text class="virtue-name" x="0" y="-1">FAITH</text>
    <text class="virtue-note" x="0" y="8">Through prayer</text>
  </g>
  <g class="virtue" transform="translate(371,391) rotate(-60)">
    <text class="virtue-name" x="0" y="-1">FIGHT</text>
    <text class="virtue-note" x="0" y="8">Determined effort</text>
  </g>
  <g class="virtue" transform="translate(314,490) rotate(-60)">
    <text class="virtue-name" x="0" y="-1">RESOURCEFULNESS</text>
    <text class="virtue-note" x="0" y="8">Proper judgement</text>
  </g>
  <g class="virtue" transform="translate(260,587) rotate(-60)">
    <text class="virtue-name" x="0" y="-1">ADAPTABILITY</text>
    <text class="virtue-note" x="0" y="8">To any situation</text>
  </g>
  <g class="virtue" transform="translate(203,684) rotate(-60)">
    <text class="virtue-name" x="0" y="-1">AMBITION</text>
    <text class="virtue-note" x="0" y="8">For noble goals</text>
  </g>

  <g class="virtue" transform="translate(552,292) rotate(60)">
    <text class="virtue-name" x="0" y="-1">PATIENCE</text>
    <text class="virtue-note" x="0" y="8">Good things take time</text>
  </g>
  <g class="virtue" transform="translate(609,391) rotate(60)">
    <text class="virtue-name" x="0" y="-1">INTEGRITY</text>
    <text class="virtue-note" x="0" y="8">Purity of intention</text>
  </g>
  <g class="virtue" transform="translate(666,490) rotate(60)">
    <text class="virtue-name" x="0" y="-1">RELIABILITY</text>
    <text class="virtue-note" x="0" y="8">Creates respect</text>
  </g>
  <g class="virtue" transform="translate(720,587) rotate(60)">
    <text class="virtue-name" x="0" y="-1">HONESTY</text>
    <text class="virtue-note" x="0" y="8">In thought and action</text>
  </g>
  <g class="virtue" transform="translate(777,684) rotate(60)">
    <text class="virtue-name" x="0" y="-1">SINCERITY</text>
    <text class="virtue-note" x="0" y="8">Keeps friends</text>
  </g>

  <g class="icon" transform="translate(346,318)" aria-label="Faith icon">
    <path d="M0,-12 L0,-6 M-9,-9 L-5,-5 M9,-9 L5,-5"/>
    <path d="M-2,14 L-2,2 L-6,-2 L-8,6 L-10,14 Z"/>
    <path d="M2,14 L2,2 L6,-2 L8,6 L10,14 Z"/>
  </g>
  <g class="icon" transform="translate(292,414)" aria-label="Fight icon">
    <rect x="-9" y="-12" width="18" height="12" rx="3"/>
    <path d="M-3,-12 V-4 M3,-12 V-4"/>
    <path d="M-8,0 V8 H8 V0"/>
    <rect x="-7" y="8" width="14" height="6"/>
  </g>
  <g class="icon" transform="translate(238,512)" aria-label="Resourcefulness icon">
    <circle cx="0" cy="0" r="10"/>
    <circle cx="0" cy="0" r="4"/>
    <path d="M0,-14 V-10 M0,10 V14 M-14,0 H-10 M10,0 H14"/>
  </g>
  <g class="icon" transform="translate(184,610)" aria-label="Adaptability icon">
    <path d="M-10,-4 A8,8 0 0 1 6,-8 L10,-4"/>
    <path d="M10,-10 V-4 H4"/>
    <path d="M10,4 A8,8 0 0 1 -6,8 L-10,4"/>
    <path d="M-10,10 V4 H-4"/>
  </g>
  <g class="icon" transform="translate(127,708)" aria-label="Ambition icon">
    <path d="M0,-14 L3,-8 L9,-7 L4.5,-3 L5.5,3 L0,0 L-5.5,3 L-4.5,-3 L-9,-7 L-3,-8 Z"/>
    <path d="M-12,-2 L-6,10 H6 L12,-2"/>
    <line x1="-6" y1="14" x2="6" y2="14"/>
  </g>

  <g class="icon" transform="translate(634,318)" aria-label="Patience icon">
    <path d="M-8,-13 H8 M-8,13 H8"/>
    <path d="M-6,-13 C-6,-4 6,-4 6,0 C6,4 -6,4 -6,13"/>
    <path d="M6,-13 C6,-4 -6,-4 -6,0 C-6,4 6,4 6,13"/>
  </g>
  <g class="icon" transform="translate(688,414)" aria-label="Integrity icon">
    <path d="M0,12 L-11,1 A6,6 0 0 1 0,-8 A6,6 0 0 1 11,1 Z"/>
  </g>
  <g class="icon" transform="translate(742,512)" aria-label="Reliability icon">
    <path d="M0,-13 L11,-9 V0 C11,7 5,11 0,13 C-5,11 -11,7 -11,0 V-9 Z"/>
    <path d="M-5,0 L-1,4 L6,-4"/>
  </g>
  <g class="icon" transform="translate(796,610)" aria-label="Honesty icon">
    <rect x="-9" y="-13" width="16" height="22" rx="1"/>
    <path d="M-5,-7 H3 M-5,-3 H3 M-5,1 H1"/>
    <path d="M3,13 V5 A3,3 0 0 1 9,5 V13"/>
  </g>
  <g class="icon" transform="translate(853,708)" aria-label="Sincerity icon">
    <circle cx="-6" cy="-7" r="4"/>
    <circle cx="6" cy="-7" r="4"/>
    <path d="M-13,12 V2 A5,5 0 0 1 -1,2 V12"/>
    <path d="M1,12 V2 A5,5 0 0 1 13,2 V12"/>
  </g>

  <g class="studio-badge">
    <circle class="badge" cx="490" cy="188" r="64"/>
    <text class="badge-name" x="490" y="185">KESTREL</text>
    <text class="badge-name" x="490" y="203">HILL</text>
  </g>

  <text class="headline" x="490" y="795"><tspan class="headline-lead">THE ORCHARD OF </tspan><tspan class="headline-key">VIRTUE</tspan></text>

  <text class="credit" x="490" y="841">Icons by Pixelgrove from Glyphyard.com</text>
</svg>
</body>
</html>
```